Birchline Septic Solutions

Would like to see some single sided ones but would also like to see some double sided with one sided only being the logo. Owners name is Tom Halvick. Phone number is 555-214-0387
Services are pumping, inspections, installs, and repairs

Contact Information for Business Card

555-241-0387 Tom Halvick Ashford, OH

```html
<!DOCTYPE html>
<html lang="en">
<head>
<meta charset="utf-8">
<title>Birchline Septic Solutions – Business Cards</title>
<link rel="stylesheet" href="https://fonts.googleapis.com/css2?family=Montserrat:wght@400;500;700;800&display=swap">
<style>
  :root {
    --teal: #06bbb4;
    --ink: #111111;
    --paper: #ffffff;
    --backdrop: #d9d9d9;
    --divider: #15b3ac;
  }
  * { box-sizing: border-box; margin: 0; padding: 0; }
  html, body { width: 1200px; height: 856px; overflow: hidden; }
  body {
    background: var(--backdrop);
    font-family: "Montserrat", Arial, sans-serif;
    position: relative;
  }
  .card {
    position: absolute;
    width: 560px;
    height: 320px;
    overflow: hidden;
    box-shadow: 0 10px 28px rgba(0,0,0,.28);
  }
  .card--front { left: 40px; top: 70px; background: var(--paper); }
  .card--back  { left: 600px; top: 466px; background: var(--teal); }

  .front-swoosh { position: absolute; inset: 0; width: 100%; height: 100%; }

  .front-brand {
    position: absolute;
    left: 120px; top: 108px;
    width: 200px;
    display: flex; align-items: center; gap: 12px;
  }
  .brand-dot {
    flex: none;
    width: 16px; height: 16px; border-radius: 50%;
    background: var(--teal);
  }
  .brand-name {
    font-weight: 800;
    font-size: 21px;
    line-height: 1.15;
    letter-spacing: .02em;
    text-transform: uppercase;
  }
  .front-brand .brand-name { color: var(--ink); }

  .front-divider {
    position: absolute;
    left: 330px; top: 62px;
    width: 1.5px; height: 100px;
    background: var(--divider);
  }
  .contact {
    position: absolute;
    left: 346px; top: 58px;
    width: 200px;
    color: var(--ink);
  }
  .contact-name {
    font-weight: 800;
    font-size: 17px;
    letter-spacing: -.01em;
    text-transform: uppercase;
  }
  .contact-name .surname { color: var(--teal); }
  .contact-role { font-size: 12.5px; margin-top: 2px; }
  .contact-lines {
    margin-top: 8px;
    font-size: 12.5px;
    line-height: 1.3;
    display: flex; gap: 6px;
  }
  .phone-icon { flex: none; width: 12px; height: 12px; margin-top: 2px; fill: var(--teal); }

  .back-brand {
    position: absolute;
    left: 0; right: 0; top: 78px;
    display: flex; justify-content: center; align-items: center; gap: 14px;
  }
  .back-brand .brand-dot { background: var(--paper); width: 20px; height: 20px; }
  .back-brand .brand-name { color: var(--paper); font-size: 30px; text-align: left; }

  .services {
    position: absolute;
    left: 0; right: 0; top: 205px;
    color: var(--paper);
    font-size: 18px;
    font-weight: 500;
    line-height: 1.45;
    text-align: center;
  }
  .tick {
    display: inline-block;
    width: 14px; height: 14px;
    vertical-align: -1px;
    margin: 0 5px;
  }
</style>
</head>
<body>

<section class="card card--front" aria-label="Business card front">
  <svg class="front-swoosh" viewBox="0 0 560 320" preserveAspectRatio="none" aria-hidden="true">
    <path d="M0 300 L400 282 C424 281 432 264 444 251 C454 241 466 237 490 236 L560 233 L560 320 L0 320 Z" fill="var(--teal)"/>
    <path d="M0 285 L388 267 C400 266 407 258 413 246 L418 248 C412 262 404 273 390 274 L0 293 Z" fill="var(--ink)"/>
  </svg>

  <div class="front-brand">
    <span class="brand-dot"></span>
    <span class="brand-name">Birchline Septic Solutions</span>
  </div>

  <div class="front-divider"></div>

  <div class="contact">
    <p class="contact-name">Tom <span class="surname">Halvick</span></p>
    <p class="contact-role">Owners</p>
    <div class="contact-lines">
      <svg class="phone-icon" viewBox="0 0 24 24" aria-hidden="true">
        <path d="M6.6 10.8a15 15 0 0 0 6.6 6.6l2.2-2.2a1 1 0 0 1 1-.25 11.4 11.4 0 0 0 3.6.57 1 1 0 0 1 1 1V20a1 1 0 0 1-1 1A17 17 0 0 1 3 4a1 1 0 0 1 1-1h3.5a1 1 0 0 1 1 1c0 1.25.2 2.45.57 3.57a1 1 0 0 1-.25 1z"/>
      </svg>
      <p>555-214-0387<br>555-241-0387 Tom<br>Halvick Ashford, OH</p>
    </div>
  </div>
</section>

<section class="card card--back" aria-label="Business card back">
  <div class="back-brand">
    <span class="brand-dot"></span>
    <span class="brand-name">Birchline<br>Septic Solutions</span>
  </div>

  <p class="services">
    <svg class="tick" viewBox="0 0 16 16" aria-hidden="true"><circle cx="8" cy="8" r="6.6" fill="none" stroke="#fff" stroke-width="1.8"/><path d="M4.8 8.2l2.2 2.2 4.4-4.6" fill="none" stroke="#fff" stroke-width="1.8"/></svg>Services are pumping<br>
    <svg class="tick" viewBox="0 0 16 16" aria-hidden="true"><circle cx="8" cy="8" r="6.6" fill="none" stroke="#fff" stroke-width="1.8"/><path d="M4.8 8.2l2.2 2.2 4.4-4.6" fill="none" stroke="#fff" stroke-width="1.8"/></svg>inspections
    <svg class="tick" viewBox="0 0 16 16" aria-hidden="true"><circle cx="8" cy="8" r="6.6" fill="none" stroke="#fff" stroke-width="1.8"/><path d="M4.8 8.2l2.2 2.2 4.4-4.6" fill="none" stroke="#fff" stroke-width="1.8"/></svg>installs
    <svg class="tick" viewBox="0 0 16 16" aria-hidden="true"><circle cx="8" cy="8" r="6.6" fill="none" stroke="#fff" stroke-width="1.8"/><path d="M4.8 8.2l2.2 2.2 4.4-4.6" fill="none" stroke="#fff" stroke-width="1.8"/></svg>and repairs
  </p>
</section>

</body>
</html>
```